Vantler Helps - Pellbrook Gives Advertising Flyer

We are a vantler club that has received funding to run a community food drive project. We need a flyer for our community project that stands out . Our community project is trying to obtain non- perishable food for low income families and the vulnerable from residents in the area.
This flyer will be need to be visible and posted on store front windows and anywhere else where local residents can see it and be informed about the project. We will need a high quality version to print and a PDF version that will be e-mailed for promotional activities.

Target Market(s)

Community

Font styles to use
Sans Serif

Requirements
Must have
• My project must have logos as specified.
Nice to have
• - Images
- eye catching and modern

```html
<!DOCTYPE html>
<html lang="en">
<head>
<meta charset="utf-8">
<title>Vantler Helps – Pellbrook Gives Food Drive Flyer</title>
<link href="https://fonts.googleapis.com/css2?family=Bebas+Neue&family=Montserrat:wght@700&family=Roboto+Condensed:wght@700&display=swap" rel="stylesheet">
<style>
  :root {
    --blue: #1c5ea7;
    --yellow: #f6c244;
    --ink: #111111;
    --white: #ffffff;
    --divider: #b9b9b9;
  }
  * { margin: 0; padding: 0; box-sizing: border-box; }
  html, body { width: 849px; height: 1200px; overflow: hidden; background: var(--white); }
  .flyer { position: relative; width: 849px; height: 1200px; overflow: hidden; background: var(--white); }

  .art { position: absolute; left: 0; top: 0; z-index: 0; }
  .layer { position: absolute; z-index: 2; }

  .brand { left: 42px; top: 50px; display: flex; align-items: center; gap: 14px; }
  .brand-dot { width: 72px; height: 72px; border-radius: 50%; background: var(--yellow); }
  .brand-name { font-family: "Montserrat", sans-serif; font-weight: 700; line-height: 1; }
  .brand-name .primary { display: block; color: var(--yellow); font-size: 31px; letter-spacing: 0.5px; }
  .brand-name .secondary { display: block; color: var(--yellow); font-size: 21px; margin-top: 7px; }

  .web-pill { left: 564px; top: 59px; width: 285px; height: 57px; background: var(--blue);
    border-radius: 29px 0 0 29px; display: flex; align-items: center; padding-left: 21px;
    font-family: "Montserrat", sans-serif; font-weight: 700; font-size: 25px; color: var(--white); }

  .rule { left: 1px; top: 153px; width: 847px; height: 4px; background: var(--blue); }

  .headline { left: 0; top: 172px; width: 849px; text-align: center;
    font-family: "Bebas Neue", sans-serif; font-weight: 400; font-size: 62px; line-height: 53px; color: var(--blue); }
  .subhead { left: 0; top: 336px; width: 849px; text-align: center;
    font-family: "Roboto Condensed", sans-serif; font-weight: 700; font-size: 32px; line-height: 44px; color: var(--yellow); }

  .appeal { left: 500px; top: 494px; width: 290px; text-align: center;
    font-family: "Bebas Neue", sans-serif; font-size: 33px; line-height: 30.5px; color: var(--ink); }
  .appeal p + p { margin-top: 6px; }

  .support-label { left: 0; top: 1044px; width: 849px; text-align: center;
    font-family: "Bebas Neue", sans-serif; font-size: 27px; letter-spacing: 0.5px; color: var(--white); }

  .partners { left: 0; top: 1073px; width: 849px; height: 99px; background: var(--white); display: flex; }
  .partner { display: flex; align-items: center; justify-content: center; gap: 8px;
    font-family: "Montserrat", sans-serif; font-weight: 700; color: var(--blue); font-size: 17px; line-height: 1.15; text-align: center; }
  .partner + .partner { border-left: 1px dashed var(--divider); margin: 8px 0; }
  .partner-1 { width: 204px; }
  .partner-2 { width: 175px; }
  .partner-3 { width: 257px; }
  .partner-4 { width: 213px; }
  .mark-circle { width: 44px; height: 44px; border-radius: 50%; background: var(--yellow); flex: none; }
  .mark-square { width: 22px; height: 22px; background: var(--blue); flex: none; }

  .footer-strip { left: 0; top: 1172px; width: 849px; height: 28px; display: flex; }
  .footer-strip .left { width: 424px; background: var(--yellow); }
  .footer-strip .right { flex: 1; background: var(--blue); }
</style>
</head>
<body>
<main class="flyer">
  <svg class="art" width="849" height="1200" viewBox="0 0 849 1200">
    <defs>
      <radialGradient id="bagTones" cx="45%" cy="45%" r="60%">
        <stop offset="0" stop-color="#2f4fb0"/>
        <stop offset="0.7" stop-color="#1f3a94"/>
        <stop offset="1" stop-color="#142a6e"/>
      </radialGradient>
    </defs>
    <rect class="blue-field" x="0" y="645" width="849" height="430" fill="var(--blue)"/>
    <circle class="photo-halo" cx="222" cy="690" r="305" fill="var(--white)"/>
    <circle class="appeal-halo" cx="646" cy="586" r="205" fill="var(--white)"/>
    <circle class="appeal-ring" cx="646" cy="586" r="195" fill="none" stroke="var(--yellow)" stroke-width="2"/>
    <circle class="photo-ring" cx="222" cy="685" r="292" fill="none" stroke="var(--yellow)" stroke-width="3"/>
    <circle class="photo-crescent" cx="236" cy="698" r="284" fill="var(--yellow)"/>
    <circle class="photo" cx="220" cy="686" r="277" fill="url(#bagTones)" role="img"
      aria-label="Photo of blue reusable shopping bags filled with donated groceries"/>
    <circle class="appeal-disc" cx="646" cy="586" r="178" fill="var(--yellow)"/>
  </svg>

  <header>
    <div class="layer brand">
      <span class="brand-dot"></span>
      <div class="brand-name">
        <span class="primary">VANTLER HELPS</span>
        <span class="secondary">PELLBROOK GIVES</span>
      </div>
    </div>
    <div class="layer web-pill">www.vph.org.au</div>
    <div class="layer rule"></div>
  </header>

  <h1 class="layer headline">Food security and<br>the COVID crisis in Pellbrook<br>you can make a difference</h1>
  <p class="layer subhead">Can you help refill Hollowfield Care’s Food Pantry?</p>

  <div class="layer appeal">
    <p>We need donations<br>of non – perishable<br>food items.</p>
    <p>Look out for our<br>bags and information<br>in your letter box</p>
  </div>

  <p class="layer support-label">Proudly supported by</p>

  <footer class="layer partners">
    <div class="partner partner-1"><span>Vantler<br>Pellbrook</span><span class="mark-circle"></span></div>
    <div class="partner partner-2"><span>PELLBROOK</span></div>
    <div class="partner partner-3"><span class="mark-square"></span><span>Kestrel Bank</span></div>
    <div class="partner partner-4"><span>The Vantler<br>Foundation</span><span class="mark-circle"></span></div>
  </footer>

  <div class="layer footer-strip"><span class="left"></span><span class="right"></span></div>
</main>
</body>
</html>
```